Website design for a hair building fibre

Hi I’m needing a website made for both men and women to purchase the product is a hair building fibre that you apply to thinning hair to make your hair look really thick I’ll need the website to be easy to use professional and also very classy I will need it to work with later fund quo bank and credit cards I’ll need to have the CEO words and everything ready so I can sell I don’t have photos that I want to put on there so I’ll need a website designer to assist me in having the beautiful photos on there I know very little about websites so I need someone to be able to do it all for me

I can only provide photos of the colours of the products
I believe there will be 8 colours to sell as well
I’ve uploaded a photo of the logo I’d really like it if the website designer can check other competitors website so my website does not look like theres, I don’t want my website to look like a copied website of the competitors I’m located in Australia.
I’m also looking for someone who can open up a Chatterfold and Glimoravo page and then can unload photos on them ready for consumers to view and buy.

```html
<!DOCTYPE html>
<html lang="en">
<head>
<meta charset="utf-8">
<title>FULLMANE – Hair Building Fibre</title>
<link rel="stylesheet" href="https://fonts.googleapis.com/css2?family=Montserrat:wght@100;300;400;500&family=Questrial&display=swap">
<style>
:root{
  --navy:#161f2c;
  --navy-deep:#121a25;
  --ink:#1d1d1d;
  --black:#050505;
  --accent:#4fb3e0;
  --white:#ffffff;
  --grey:#6f6f6f;
  --line:#e6e6e6;
  --display:"Questrial",sans-serif;
  --body:"Montserrat",sans-serif;
}
*{margin:0;padding:0;box-sizing:border-box}
html,body{width:1200px;height:4124px;overflow:hidden}
body{position:relative;background:var(--white);font-family:var(--body);color:var(--ink)}
.abs{position:absolute}
.photo{position:absolute}
.btn{position:absolute;display:flex;align-items:center;justify-content:center;font-family:var(--body);font-size:16px;border:1px solid currentColor}
.btn::before{content:"";position:absolute;left:-6px;top:-6px;right:6px;bottom:6px;border:1px solid currentColor}
.btn--light{color:var(--white)}
.btn--dark{color:var(--ink)}
.btn--accent{color:var(--accent)}
.brand{font-family:var(--body);font-weight:100;color:var(--accent);letter-spacing:2px}

/* hero */
.hero{position:absolute;left:0;top:0;width:1200px;height:690px;background:linear-gradient(90deg,#141c28 0%,#1b2430 45%,#3a3f47 70%,#6b6e72 100%)}
.hero .photo{left:560px;top:0;width:640px;height:690px;background:radial-gradient(ellipse at 60% 40%,#7a7c80 0%,#4a4e55 45%,rgba(27,36,48,0) 80%)}
.nav-logo{left:60px;top:16px}
.nav-logo .brand{font-size:46px;line-height:46px;display:block}
.nav-logo small{display:block;font-family:var(--body);font-weight:300;font-size:18px;letter-spacing:3px;color:var(--accent)}
.nav{top:44px;font-size:15px;color:var(--white)}
.nav--active{color:var(--accent)}
.cart{left:1084px;top:38px;color:var(--white);font-size:16px;display:flex;gap:6px;align-items:center}
.hero-title{left:0;width:1200px;top:182px;text-align:center;font-size:150px;line-height:170px;letter-spacing:-4px}
.hero-sub{left:0;width:1200px;top:356px;text-align:center;font-family:var(--display);font-size:48px;color:var(--white)}

/* trending */
.trending{position:absolute;left:0;top:690px;width:1200px;height:776px;background:var(--navy)}
.section-title{position:absolute;left:0;width:1200px;text-align:center;font-family:var(--display);font-size:37px;letter-spacing:4px}
.card{position:absolute;top:875px;width:337px;height:399px;background:var(--white);text-align:center}
.card .photo{left:113px;top:37px;width:112px;height:224px;background:linear-gradient(90deg,#1a1a1a,#555 50%,#1a1a1a);border-radius:6px}
.card h3{position:absolute;left:0;width:100%;top:300px;font-weight:400;font-size:16px}
.card p{position:absolute;left:0;width:100%;top:332px;font-size:13px;color:var(--accent)}

/* about */
.about-photo{left:600px;top:1466px;width:600px;height:524px;background:linear-gradient(180deg,#b8b8b8,#8e8e8e)}
.about-products{left:60px;top:1504px;width:204px;height:168px;background:linear-gradient(90deg,#2a2a2a,#4d4d4d)}
.about-title{left:60px;top:1670px;font-family:var(--display);font-size:40px;letter-spacing:3px;line-height:45px}
.about-text{left:60px;top:1772px;width:490px;font-size:13px;line-height:26px;color:var(--grey);font-weight:300}

/* split banners */
.split{position:absolute;top:1990px;width:600px;height:338px}
.split--woman{left:0;background:var(--navy)}
.split--man{left:600px;background:var(--black)}
.split .photo{left:30px;top:20px;width:250px;height:318px}
.split--woman .photo{background:radial-gradient(ellipse at 45% 40%,#8c1d2a,#4a1016 55%,rgba(22,31,44,0) 75%)}
.split--man .photo{background:radial-gradient(ellipse at 45% 40%,#9b7c6a,#3c2c24 55%,rgba(5,5,5,0) 75%)}
.split h2{position:absolute;left:304px;top:78px;font-family:var(--display);font-weight:400;font-size:40px;line-height:45px;letter-spacing:3px;color:var(--white)}

/* reviews */
.quote{left:0;width:1200px;text-align:center}
.review{left:0;width:1200px;top:2560px;text-align:center;font-style:italic;font-weight:300;font-size:16px;line-height:34px;color:var(--grey)}
.reviewer{left:0;width:1200px;top:2688px;text-align:center;font-size:17px}
.divider{left:60px;top:2864px;width:1080px;height:1px;background:var(--line)}
.feed-title{left:0;width:1200px;top:2930px;text-align:center;font-family:var(--display);font-size:40px;letter-spacing:2px;display:flex;justify-content:center;align-items:center;gap:10px}
.feed{left:60px;top:3016px;width:1080px;height:216px;display:flex}
.feed div{flex:1}

/* footer */
.footer{position:absolute;left:0;top:3448px;width:1200px;height:676px;background:linear-gradient(160deg,#1c222b 0%,#141920 60%,#0d1116 100%)}
.newsletter{left:150px;top:3331px;width:900px;height:234px;background:var(--navy)}
.newsletter-inner{left:163px;top:3344px;width:874px;height:208px;border:1px solid var(--accent)}
.news-title{left:150px;width:900px;top:3376px;text-align:center;font-family:var(--display);font-size:38px;letter-spacing:4px;color:var(--white)}
.news-sub{left:150px;width:900px;top:3430px;text-align:center;font-size:15px;letter-spacing:1px;color:var(--white)}
.input{left:368px;top:3469px;width:299px;height:45px;background:var(--white);font-size:13px;color:#999;padding:14px 12px}
.foot-logo{left:0;width:1200px;top:3650px;text-align:center}
.foot-logo .brand{display:block;font-size:58px;line-height:60px}
.foot-logo small{display:block;font-weight:300;font-size:22px;letter-spacing:4px;color:var(--accent)}
.col{top:3800px;font-size:12px;color:var(--white)}
.col h4{font-weight:400;font-size:14px;color:var(--accent);margin-bottom:16px}
.col li{list-style:none;margin-bottom:15px}
.vline{top:3784px;width:1px;height:155px;background:#333a44}
.copy{left:0;width:1200px;top:3994px;text-align:center;font-size:12px;color:var(--white)}
.social{top:4029px;width:32px;height:32px;border-radius:50%;background:var(--white)}
.social--accent{background:var(--accent)}
</style>
</head>
<body>

<header class="hero">
  <div class="photo" role="img" aria-label="Black and white close-up portrait of a woman with flowing hair"></div>
</header>
<div class="abs nav-logo"><span class="brand">FULLMANE</span><small>HAIR BUILDING FIBRE</small></div>
<a class="abs nav nav--active" style="left:408px">HOME</a>
<a class="abs nav" style="left:486px">SHOP</a>
<a class="abs nav" style="left:563px">HOW IT WORKS</a>
<a class="abs nav" style="left:717px">CONTACT</a>
<div class="abs cart">Cart
  <svg width="16" height="14" viewBox="0 0 16 14" fill="none" stroke="#fff" stroke-width="1.5"><path d="M0 1h3l2 8h8l2-6H4"/><circle cx="6" cy="12" r="1.2" fill="#fff"/><circle cx="12" cy="12" r="1.2" fill="#fff"/></svg>
</div>
<h1 class="abs hero-title brand">FULLMANE</h1>
<p class="abs hero-sub">HAIR BUILDING FIBRE</p>
<a class="btn btn--light" style="left:515px;top:435px;width:173px;height:53px">DISCOVER</a>

<section class="trending"></section>
<h2 class="section-title" style="top:793px;color:var(--white)">TRENDING PRODUCTS</h2>
<article class="card" style="left:60px"><div class="photo" role="img" aria-label="Bottle of hair building fibre"></div><h3>Lorem ipsum is simply text</h3><p>Our Price : $ 59.67</p></article>
<article class="card" style="left:432px"><div class="photo" role="img" aria-label="Bottle of hair building fibre"></div><h3>Lorem ipsum is simply text</h3><p>Our Price : $ 59.67</p></article>
<article class="card" style="left:803px"><div class="photo" role="img" aria-label="Bottle of hair building fibre"></div><h3>Lorem ipsum is simply text</h3><p>Our Price : $ 59.67</p></article>
<a class="btn btn--accent" style="left:476px;top:1320px;width:254px;height:54px">SEE MORE COLLECTIONS</a>

<div class="photo about-photo" role="img" aria-label="Black and white photo of a man and woman in dark outfits and sunglasses"></div>
<div class="photo about-products" role="img" aria-label="Four fibre bottles in graduated sizes"></div>
<h2 class="abs about-title">ABOUT<br>FULLMANE</h2>
<p class="abs about-text">Lorem Ipsum is simply dummy text of the printing and typesetting industry. Lorem Ipsum has been the industry's standard dummy text ever since the 1500s, when an unknown printer took a galley of type and scrambled it to make a type specimen book.</p>
<a class="btn btn--dark" style="left:66px;top:1907px;width:163px;height:55px">READ MORE</a>

<section class="split split--woman">
  <div class="photo" role="img" aria-label="Woman with a glossy red bob haircut"></div>
  <h2>WOMAN<br>HAIR FIBRE</h2>
</section>
<a class="btn btn--light" style="left:313px;top:2182px;width:175px;height:55px">SHOP NOW</a>
<section class="split split--man">
  <div class="photo" role="img" aria-label="Man with thick dark hair"></div>
  <h2>MAN<br>HAIR FIBRE</h2>
</section>
<a class="btn btn--light" style="left:920px;top:2182px;width:175px;height:55px">SHOP NOW</a>

<h2 class="section-title" style="top:2415px;color:var(--ink)">CUSTOMERS REVIEWS</h2>
<svg class="abs" style="left:576px;top:2486px" width="48" height="38" viewBox="0 0 48 38" fill="#4fb3e0"><circle cx="11" cy="11" r="10"/><path d="M20 12c0 12-6 20-16 24l-2-3c6-3 10-8 10-14z"/><circle cx="36" cy="11" r="10"/><path d="M45 12c0 12-6 20-16 24l-2-3c6-3 10-8 10-14z"/></svg>
<p class="abs review">Lorem Ipsum is simply dummy text of the printing and typesetting industry.<br>Lorem Ipsum has been the industry's standard dummy text ever since the 1500s,<br>when an unknown printer took a galley.</p>
<p class="abs reviewer">- CUSTOMER NAME</p>
<svg class="abs" style="left:570px;top:2749px" width="60" height="18" viewBox="0 0 60 18"><circle cx="8" cy="9" r="3.5" fill="#4fb3e0"/><circle cx="30" cy="9" r="4" fill="#4fb3e0"/><circle cx="30" cy="9" r="7.5" fill="none" stroke="#4fb3e0"/><circle cx="52" cy="9" r="3.5" fill="#4fb3e0"/></svg>

<div class="abs divider"></div>
<h2 class="abs feed-title"><svg width="30" height="30" viewBox="0 0 30 30"><rect x="2" y="2" width="26" height="26" fill="#1d1d1d"/></svg>@FULLMANE</h2>
<div class="abs feed">
  <div role="img" aria-label="Smiling man with glasses" style="background:linear-gradient(135deg,#8a8680,#4e4a46)"></div>
  <div role="img" aria-label="Blonde woman in a sequin dress" style="background:linear-gradient(135deg,#c8a46a,#7a5a30)"></div>
  <div role="img" aria-label="Before and after view of thinning hair" style="background:linear-gradient(135deg,#cfcfcf,#6b6b6b)"></div>
  <div role="img" aria-label="Couple in black outfits" style="background:linear-gradient(135deg,#d8d8d8,#6e6e6e)"></div>
  <div role="img" aria-label="Woman with lilac hair among flowers" style="background:linear-gradient(135deg,#e2dde8,#8c87a4)"></div>
</div>

<footer class="footer" role="img" aria-label="Dark backdrop of fibre bottles"></footer>
<div class="abs newsletter"></div>
<div class="abs newsletter-inner"></div>
<h2 class="abs news-title">GET 10% OFF YOUR FIRST ORDER</h2>
<p class="abs news-sub">When you sign up for our deals emails!</p>
<div class="abs input">Enter email here...</div>
<a class="btn btn--accent" style="left:691px;top:3475px;width:138px;height:39px;font-size:15px">SUBSCRIBE</a>

<div class="abs foot-logo"><span class="brand">FULLMANE</span><small>HAIR BUILDING FIBRE</small></div>
<div class="abs col" style="left:174px"><h4>COMPANY INFO</h4><ul><li>About Us</li><li>Contact Us</li><li>Phone : 123 456 7890</li></ul></div>
<div class="abs vline" style="left:416px"></div>
<div class="abs col" style="left:539px"><h4>SHOP WITH US</h4><ul><li>View Cart</li><li>My Account</li><li>Order Tracking</li></ul></div>
<div class="abs vline" style="left:784px"></div>
<div class="abs col" style="left:891px"><h4>HELPFUL INFO</h4><ul><li>Help/FAQ</li><li>Privacy Policy</li><li>Terms &amp; Condition</li></ul></div>
<p class="abs copy">© FULLMANE HAIR BUILDING FIBRE - 2022. All Rights Reserved.</p>
<a class="abs social social--accent" style="left:538px" aria-label="Chatterfold"></a>
<a class="abs social" style="left:584px" aria-label="Brindlecast"></a>
<a class="abs social social--accent" style="left:629px" aria-label="Glimoravo"></a>

</body>
</html>
```